Business card for denture clinic Gumlyssa

We need a new business card with our new logo. We are a denture clinic in New Zealand with our target market being 45+ years old. We would need a space on the back to write our patients next appointment on. We would space for only one appointment rather than a list. We will attach a photo showing an example of this. But of course, we would like to see your twist on this. We want it to be bold and easy to read and a good mixture of professional but modern. We have attached our logo to be used on the card.

Target Market(s)

People aged 45+ needing dentures

Industry/Entity Type

Dental

Contact Information for Business Card

We want our logo on the front and the space to write an appointment on the back. I've attached an example our our old business card showing this. We need to have the technicians details on the front.

Font styles to use
Sans Serif

Colors
0255a3
919191
fbfbfb

Requirements
Must have
• The following details:
• Ravi Pelling BDT, PGDipCDentTech Marlow
• Dental Prosthetist
• Phone numbers: 0800 47 2150
• 09 571 3294
• Email: ravi@gumlyssa.co.nz
• www.gumlyssa.co.nz
• Address: 418 Whiroa Road
• Kauriwhenua East
• Auckland 0610
Nice to have
• We would like our business cards to have more than just two colours as we want them to be more vibrant. We have uploaded an example of a business card we liked that showed this.

```html
<!DOCTYPE html>
<html lang="en">
<head>
<meta charset="utf-8">
<title>Gumlyssa Business Card</title>
<link rel="stylesheet" href="https://fonts.googleapis.com/css2?family=Karla:wght@400;500;700&display=swap">
<style>
  :root {
    --brand-blue: #1170b6;
    --brand-blue-deep: #0255a3;
    --brand-grey: #919191;
    --accent-sky: #bfe0f5;
    --paper: #fbfbfb;
    --backdrop: #ece9e4;
    --text-light: #ffffff;
    --rule: #9a9a9a;
  }
  * { box-sizing: border-box; margin: 0; padding: 0; }
  html, body {
    width: 1200px;
    height: 1200px;
    overflow: hidden;
    background: var(--backdrop);
    font-family: "Karla", Arial, sans-serif;
  }
  .stage { position: relative; width: 1200px; height: 1200px; }
  .card {
    position: absolute;
    width: 780px;
    height: 470px;
    background: var(--paper);
    box-shadow: 0 14px 30px rgba(0,0,0,0.22);
    overflow: hidden;
  }
  .card--front { left: 120px; top: 70px; }
  .card--back  { left: 300px; top: 650px; }

  /* Front */
  .front-band {
    position: absolute;
    left: 0; right: 0;
    background: var(--brand-blue);
    color: var(--text-light);
  }
  .front-band--top { top: 0; height: 150px; }
  .front-band--bottom { bottom: 0; height: 175px; background: var(--brand-blue-deep); }

  .technician {
    position: absolute;
    left: 180px;
    top: 70px;
    display: flex;
    align-items: flex-start;
    gap: 12px;
  }
  .technician__name {
    font-size: 32px;
    font-weight: 700;
    line-height: 1;
  }
  .technician__details {
    font-size: 19px;
    line-height: 1.45;
    margin-top: -4px;
  }

  .brand {
    display: flex;
    align-items: center;
    justify-content: center;
    gap: 18px;
  }
  .brand__square { width: 62px; height: 62px; flex: none; }
  .brand__name {
    font-size: 52px;
    font-weight: 700;
    letter-spacing: 3px;
    text-transform: uppercase;
    line-height: 1;
  }
  .front-brand {
    position: absolute;
    left: 0; right: 0;
    top: 150px;
    height: 145px;
  }
  .front-brand .brand { height: 100%; }
  .front-brand .brand__square { background: var(--brand-grey); }
  .front-brand .brand__name { color: var(--brand-blue); }

  .contact {
    position: absolute;
    left: 0; right: 0;
    top: 18px;
    text-align: center;
    font-size: 19px;
    line-height: 1.7;
  }
  .contact__label { font-weight: 700; color: var(--accent-sky); }

  /* Back */
  .back-band {
    position: absolute;
    left: 0; right: 0; top: 0;
    height: 312px;
    background: var(--brand-blue);
  }
  .back-band .brand { height: 100%; padding-top: 10px; }
  .back-band .brand__square { background: var(--text-light); }
  .back-band .brand__name { color: var(--text-light); }
  .back-accent {
    position: absolute;
    left: 0; right: 0; top: 312px;
    height: 6px;
    background: var(--brand-grey);
  }

  .appointment {
    position: absolute;
    left: 0; right: 0;
    top: 318px;
    bottom: 0;
    color: var(--brand-grey);
  }
  .appointment__title {
    text-align: center;
    font-size: 24px;
    margin-top: 12px;
    letter-spacing: 0.3px;
  }
  .appointment__fields {
    display: flex;
    justify-content: center;
    align-items: flex-end;
    gap: 26px;
    margin-top: 44px;
    font-size: 24px;
  }
  .field { display: flex; align-items: flex-end; gap: 6px; }
  .field__line {
    display: inline-block;
    border-bottom: 1px dotted var(--rule);
    height: 22px;
  }
  .field__line--day,
  .field__line--month,
  .field__line--year { width: 72px; }
  .field__line--time { width: 245px; }
  .field__slash { padding: 0 2px; }
</style>
</head>
<body>
<main class="stage">

  <section class="card card--front" aria-label="Business card front">
    <div class="front-band front-band--top">
      <div class="technician">
        <span class="technician__name">Ravi Pelling</span>
        <span class="technician__details">
          BDT, PGDipCDentTech Marlow<br>
          Dental Prosthetist
        </span>
      </div>
    </div>

    <div class="front-brand">
      <div class="brand">
        <span class="brand__square"></span>
        <span class="brand__name">Gumlyssa</span>
      </div>
    </div>

    <div class="front-band front-band--bottom">
      <p class="contact">
        <span class="contact__label">P:</span> 0800 47 2150, 09 571 3294<br>
        <span class="contact__label">E:</span> ravi@gumlyssa.co.nz<br>
        <span class="contact__label">W:</span> www.gumlyssa.co.nz<br>
        <span class="contact__label">A:</span> 418 Whiroa Road, Kauriwhenua East, Auckland 0610
      </p>
    </div>
  </section>

  <section class="card card--back" aria-label="Business card back">
    <div class="back-band">
      <div class="brand">
        <span class="brand__square"></span>
        <span class="brand__name">Gumlyssa</span>
      </div>
    </div>
    <div class="back-accent"></div>

    <div class="appointment">
      <p class="appointment__title">your next appointment</p>
      <div class="appointment__fields">
        <span class="field">
          date
          <span class="field__line field__line--day"></span><span class="field__slash">/</span><span class="field__line field__line--month"></span><span class="field__slash">/</span><span class="field__line field__line--year"></span>
        </span>
        <span class="field">
          time
          <span class="field__line field__line--time"></span>
        </span>
      </div>
    </div>
  </section>

</main>
</body>
</html>
```